Creative designs Needed! Dieting Tips for Nurses

Need a creative design for my first book that is targeted to nurses that want to lose weight.
THE TITLE OF MY BOOK IS:
Lanyard Lunchbox Reset:
9 Waistline Tricks Each Caregiver Should Master!

- My audience is female.

- My colors for my business are red, black, gray and white however feel free to use other colors

- The cover should note there is Free Bonus Content.

- The book cover should have a fun modern feel to it.

- Since the title is talking about time. I think there should be some sort of clock in the design. Not an actual clock but a clock design.

- Please let me know if you need anything from me to complete your design. I go by Coach Bex.

- Subject of book is dieting tips for nurses

Nurses

Health And Wellness

Serif

ec1f27
1b1b1b
dddddd

• List the Free Bonus Content label on the front cover
• Must keep in mind there will be sequels to this book for other target markets
• • Should be creative, modern
• • Please try not to use stock images with just the text for this design - I am looking for something creative and unique.
• • Something that plays with the idea of time, think clock.
• • Need something out the box!!
• • Think diversity in the people if you do opt to use images - Would prefer if you steer clear of regular photos of people
• • If you do use an image of a nurse, please note nurses mostly wear scrubs today - so think about that in your concepts
• The design should be clever
• Although I selected the 3 colors feel free to explore other colors and those 3 colors do not have to be the dominate colors.
• The book design should pop out to people when they see it.

```html
<!DOCTYPE html>
<html lang="en">
<head>
<meta charset="utf-8">
<title>Lanyard Lunchbox Reset – Book Cover</title>
<link rel="stylesheet" href="https://fonts.googleapis.com/css2?family=Archivo+Black&family=Bebas+Neue&display=swap">
<style>
  :root {
    --cover-red: #ec1f27;
    --ink-black: #000000;
    --paper-white: #ffffff;
    --swirl-light: #fbd3c6;
  }
  html, body {
    margin: 0;
    padding: 0;
    overflow: hidden;
    background: var(--cover-red);
  }
  .cover {
    position: relative;
    width: 750px;
    height: 1200px;
    overflow: hidden;
    background: var(--cover-red);
    color: var(--paper-white);
  }
  .time-swirl,
  .clock-ticks {
    position: absolute;
    left: 0;
    top: 0;
  }
  .book-title {
    position: absolute;
    left: 8px;
    top: 40px;
    margin: 0;
    font-family: "Archivo Black", "Arial Black", sans-serif;
    font-weight: 400;
    text-transform: uppercase;
    line-height: 0.98;
    letter-spacing: 1px;
    font-size: 50px;
  }
  .book-title .title-line {
    display: block;
    white-space: nowrap;
  }
  .book-title .title-gap {
    display: inline-block;
    width: 36px;
  }
  .book-subtitle {
    position: absolute;
    left: 114px;
    top: 888px;
    margin: 0;
    font-family: "Archivo Black", "Arial Black", sans-serif;
    font-weight: 400;
    font-size: 41px;
    line-height: 1.2;
    text-transform: uppercase;
    white-space: nowrap;
  }
  .book-subtitle .count {
    font-size: 56px;
    line-height: 1;
  }
  .bonus-band {
    position: absolute;
    left: 0;
    top: 1102px;
    width: 100%;
    height: 48px;
    background: var(--ink-black);
  }
  .bonus-label {
    margin: 0;
    padding-left: 22px;
    font-family: "Bebas Neue", "Oswald", sans-serif;
    font-size: 46px;
    line-height: 50px;
    letter-spacing: 0.5px;
  }
</style>
</head>
<body>
  <main class="cover">
    <svg class="time-swirl" width="750" height="1200" viewBox="0 0 750 1200"
         role="img" aria-label="Typographic swirl: the title word repeated in fading arcs, sweeping like a clock hand">
      <defs>
        <radialGradient id="swirlFade" cx="24" cy="144" r="624" gradientUnits="userSpaceOnUse">
          <stop offset="0" stop-color="var(--paper-white)" stop-opacity="0.95"/>
          <stop offset="0.35" stop-color="var(--swirl-light)" stop-opacity="0.75"/>
          <stop offset="1" stop-color="var(--swirl-light)" stop-opacity="0.2"/>
        </radialGradient>
      </defs>
      <path d="M 24 144 L 648 144 A 624 624 0 0 1 0 768 L 0 144 Z"
            fill="url(#swirlFade)" opacity="0.7"/>
    </svg>

    <svg class="clock-ticks" width="750" height="1200" viewBox="0 0 750 1200" aria-hidden="true">
      <g stroke="var(--paper-white)" stroke-width="4">
        <line x1="692" y1="127" x2="750" y2="127"/>
        <line x1="650" y1="366" x2="750" y2="402"/>
        <line x1="530" y1="573" x2="578" y2="614"/>
        <line x1="346" y1="728" x2="410" y2="836"/>
        <line x1="118" y1="812" x2="129" y2="862"/>
      </g>
    </svg>

    <h1 class="book-title">
      <span class="title-line">Lanyard<span class="title-gap"></span>Lunchbox</span>
      <span class="title-line">Reset:</span>
    </h1>

    <h2 class="book-subtitle">
      <span class="count">9</span> Waistline Tricks<br>
      Each Caregiver<br>
      Should Master!
    </h2>

    <div class="bonus-band">
      <p class="bonus-label">Free Bonus Content</p>
    </div>
  </main>
</body>
</html>
```